International Petrochemical business needs a web design for Tessaro Desk system

We need a web design for a "Tessaro Desk" system for an international petrochemical company. The web site is used internally within the company. It is hosted by an internal department which provides government permit request service for other departments.

We would like to see designs of two pages using color light blue. (home page, internal page as attached).
Home Page:
1. Header has a background image and small animation. Header on home page can be taller than the header of the internal page.
2. Layout as attached.

Internal Page:
1. Header can use the same background image as the home page and can be shorter to utilize the page for content.
2. The blue icon behind every captions represent an icon. When user move mouse over this icon, it displays the caption in Thai language as a tooltip. This icon needs to be redesign.

The final design should communicate the followings:
- Excellent service provided system in terms of time and accurary
- Rapid growth of business via building petrochemical refinery plant

For Internal Page, the blue circle behind every captions represent an icon. When mouse over this icon, a tool tip showing the caption in Thai language is shown. Please also design this icon..

There are more feedbacks from customer as followed:

1. Banner should consists of 
    1.1 "Approved" stamp on paper
    1.2 An image of Garuda. It is used on every government documents in Thailand
    1.3 Image of petrochemical plant
2. Each menu item (Home, Permit, Search, etc) should have different colors. Drop down menu will use the same color as its parent menu item.
3. Overall tone of the web page should be light blue with background of the body the web page in white
4. "New Request" button should use green color with icon on it
5. Table header of each box in the body of the page should use dark blue background with text in white

Please kindly submit your revisions.
Thank you.

Reason: We get some late feedbacks from customers which was just updated to all designers.

• 1. Design for 1024x768 screen resolution
2. Use light blue theme
3. Background of header where the company logo is must have white background

```html
<!DOCTYPE html>
<html lang="en">
<head>
<meta charset="utf-8">
<title>Tessaro Desk System</title>
<link href="https://fonts.googleapis.com/css2?family=Ubuntu:wght@300;400;500&display=swap" rel="stylesheet">
<style>
:root{
  --sky:#0a9fdc;
  --sky-dark:#0686c2;
  --navy-top:#2c4aa6;
  --navy-bottom:#1a2d7c;
  --red:#e8232a;
  --red-dark:#c9161c;
  --text:#555b63;
  --rule:#e3e6ea;
  --row-alt:#f6f7f8;
  --bg-top:#e9eaec;
  --bg-mid:#f3f3f4;
  --grey-icon:#7a7d82;
}
*{box-sizing:border-box;margin:0;padding:0}
html,body{width:1200px;height:966px;overflow:hidden}
body{font-family:'Ubuntu',sans-serif;color:var(--text);background:#fff;position:relative}
.backdrop-top{position:absolute;left:0;top:0;width:1200px;height:442px;background:var(--bg-top)}
.backdrop-mid{position:absolute;left:0;top:442px;width:1200px;height:436px;background:var(--bg-mid)}

.topbar{position:absolute;left:200px;top:0;width:800px;height:55px;background:#fff;box-shadow:0 1px 3px rgba(0,0,0,.15);display:flex;align-items:center;justify-content:space-between}
.brand{display:flex;align-items:center;gap:6px;padding-left:16px;font-weight:500;font-size:11px;color:var(--sky);line-height:1}
.brand-dot{width:20px;height:22px;border-radius:50%;background:var(--sky)}
.main-nav{display:flex;height:55px}
.main-nav a{display:flex;align-items:center;padding:0 16px;font-size:15px;color:var(--sky);text-decoration:none;border-left:1px solid #eceef0}
.main-nav a:first-child{border-left:none}
.main-nav a.active{background:var(--red);color:#fff;padding:0 16px}

.hero-art{position:absolute;left:210px;top:80px;width:780px;height:238px;background:linear-gradient(180deg,rgba(10,159,220,0) 0%,rgba(10,159,220,.55) 55%,#1384b8 100%);clip-path:polygon(0 100%,10% 80%,22% 60%,30% 25%,45% 10%,60% 30%,74% 0,85% 20%,92% 70%,100% 100%)}
.hero-title{position:absolute;left:392px;top:246px;width:416px;height:40px;background:var(--red);color:#fff;font-weight:300;font-size:34px;display:flex;align-items:center;justify-content:center;letter-spacing:-.5px}
.hero-sub{position:absolute;left:334px;top:286px;width:532px;height:32px;background:var(--sky);color:#fff;font-size:21px;font-weight:300;display:flex;align-items:center;justify-content:center;letter-spacing:-.5px}

.panel{position:absolute;left:200px;top:318px;width:800px;height:584px;background:#fff;box-shadow:0 0 3px rgba(0,0,0,.12)}

.section-title{position:absolute;font-size:21px;color:var(--sky);font-weight:400;letter-spacing:-.3px}
.box{position:absolute;border:1px solid var(--rule);border-top:none;background:#fff}
table{width:100%;border-collapse:collapse;font-size:12px}
th{height:32px;text-align:left;font-weight:400;font-size:13px;color:#fff;padding-left:13px;border-left:1px solid rgba(255,255,255,.15)}
th:first-child{border-left:none}
.navy th{background:linear-gradient(180deg,var(--navy-top),var(--navy-bottom))}
.sky th{background:linear-gradient(180deg,#17acea,var(--sky-dark))}
td{height:32px;padding-left:13px;border-left:1px solid #eef0f2}
td:first-child{border-left:none}
tbody tr:nth-child(odd) td{background:var(--row-alt)}
.pager{height:32px;display:flex;align-items:center;justify-content:flex-end;gap:6px;padding-right:11px}
.pager span{width:16px;height:16px;border:1px solid #d6d9dc;font-size:11px;color:#a0a5ab;display:flex;align-items:center;justify-content:center;background:#fff}
.pager span.on{background:var(--sky);color:#fff;border-color:var(--sky)}
.pager span.next{background:var(--sky);border-color:var(--sky)}
.pager svg{width:8px;height:8px}

.new-request{position:absolute;left:405px;top:383px;width:387px;height:48px;background:linear-gradient(180deg,var(--red),var(--red-dark));color:#fff;font-size:26px;display:flex;align-items:center;gap:16px;padding-left:12px}
.new-request svg{width:26px;height:26px}

.footer-brand{position:absolute;left:200px;top:916px;display:flex;align-items:center;gap:5px;font-size:11px;font-weight:500;color:var(--grey-icon)}
.footer-brand .brand-dot{background:var(--grey-icon)}
.copyright{position:absolute;left:465px;top:929px;font-size:11px;color:#666}
.social{position:absolute;right:200px;top:925px;display:flex;gap:4px}
.social span{width:22px;height:22px;border-radius:50%;background:var(--grey-icon)}
</style>
</head>
<body>
<div class="backdrop-top"></div>
<div class="backdrop-mid"></div>

<header class="topbar">
  <div class="brand"><span class="brand-dot"></span>VELMORA<br>PETROCHEMICAL</div>
  <nav class="main-nav">
    <a class="active" href="#">Home</a>
    <a href="#">Permits</a>
    <a href="#">Search</a>
    <a href="#">Report</a>
    <a href="#">Admin</a>
    <a href="#">Help</a>
  </nav>
</header>

<div class="hero-art" role="img" aria-label="Blue silhouettes of oil pump jacks and a refinery skyline"></div>
<div class="hero-title">TESSARO DESK SYSTEM</div>
<div class="hero-sub">FOR AN INTERNATIONAL PETROCHEMICAL COMPANY</div>

<main class="panel">
  <h2 class="section-title" style="left:10px;top:9px">New Requests</h2>
  <div class="box navy" style="left:10px;top:48px;width:387px">
    <table>
      <colgroup><col style="width:115px"><col style="width:137px"><col></colgroup>
      <thead><tr><th>Request No.</th><th>Requested Date</th><th>Branch</th></tr></thead>
      <tbody>
        <tr><td>56-0003</td><td>20/4/2013</td><td>GC1</td></tr>
        <tr><td>56-0004</td><td>21/4/2013</td><td>GC2</td></tr>
      </tbody>
    </table>
    <div class="pager"><span><svg viewBox="0 0 8 8"><path d="M5 1 2 4l3 3" fill="none" stroke="#a0a5ab"/></svg></span><span class="on">1</span><span>2</span><span>3</span><span>5</span><span>10</span><span>...</span><span class="next"><svg viewBox="0 0 8 8"><path d="M3 1l3 3-3 3" fill="none" stroke="#fff" stroke-width="1.3"/></svg></span></div>
  </div>

  <h2 class="section-title" style="left:406px;top:9px">My Working Requests</h2>
  <div class="box navy" style="left:405px;top:48px;width:387px">
    <table>
      <colgroup><col style="width:111px"><col style="width:138px"><col></colgroup>
      <thead><tr><th>Request No.</th><th>Requested Date</th><th>Status</th></tr></thead>
      <tbody>
        <tr><td>55-0200</td><td>25/3/2013</td><td>Waiting for Progress</td></tr>
        <tr><td>55-0210</td><td>23/3/2013</td><td>In Progress</td></tr>
      </tbody>
    </table>
    <div class="pager"><span><svg viewBox="0 0 8 8"><path d="M5 1 2 4l3 3" fill="none" stroke="#a0a5ab"/></svg></span><span class="on">1</span><span>2</span><span>3</span><span>5</span><span>10</span><span>...</span><span class="next"><svg viewBox="0 0 8 8"><path d="M3 1l3 3-3 3" fill="none" stroke="#fff" stroke-width="1.3"/></svg></span></div>
  </div>

  <h2 class="section-title" style="left:10px;top:194px">Expiring Permits</h2>
  <div class="box sky" style="left:10px;top:232px;width:782px">
    <table>
      <colgroup><col style="width:108px"><col style="width:124px"><col style="width:157px"><col style="width:118px"><col style="width:159px"><col></colgroup>
      <thead><tr><th>Permit No.</th><th>Expire Date</th><th>Permit Name</th><th>Branch</th><th>Required Time (Day)</th><th>Due Date</th></tr></thead>
      <tbody>
        <tr><td>56-0003</td><td>20/4/2013</td><td>Permit Name ###10</td><td>GC1</td><td>30 Days</td><td>- 40 Days</td></tr>
        <tr><td>56-0004</td><td>21/4/2013</td><td>Permit Name ###10</td><td>GC2</td><td>60 Days</td><td>- 15 Days</td></tr>
      </tbody>
    </table>
    <div class="pager" style="padding-right:21px"><span><svg viewBox="0 0 8 8"><path d="M5 1 2 4l3 3" fill="none" stroke="#a0a5ab"/></svg></span><span class="on">1</span><span>2</span><span>3</span><span>5</span><span>10</span><span>...</span><span class="next"><svg viewBox="0 0 8 8"><path d="M3 1l3 3-3 3" fill="none" stroke="#fff" stroke-width="1.3"/></svg></span></div>
  </div>

  <h2 class="section-title" style="left:10px;top:374px">New Requests</h2>
  <div class="box navy" style="left:10px;top:413px;width:387px">
    <table>
      <colgroup><col style="width:115px"><col style="width:137px"><col></colgroup>
      <thead><tr><th>Request No.</th><th>Requested Date</th><th>Status</th></tr></thead>
      <tbody>
        <tr><td>56-0001</td><td>20/4/2013</td><td>In Progress</td></tr>
        <tr><td>56-0002</td><td>21/4/2013</td><td>In Progress</td></tr>
        <tr><td>56-0002</td><td>21/4/2013</td><td>In Progress</td></tr>
      </tbody>
    </table>
    <div class="pager"><span><svg viewBox="0 0 8 8"><path d="M5 1 2 4l3 3" fill="none" stroke="#a0a5ab"/></svg></span><span class="on">1</span><span>2</span><span>3</span><span>5</span><span>10</span><span>...</span><span class="next"><svg viewBox="0 0 8 8"><path d="M3 1l3 3-3 3" fill="none" stroke="#fff" stroke-width="1.3"/></svg></span></div>
  </div>

  <a class="new-request">
    <svg viewBox="0 0 26 26"><circle cx="13" cy="13" r="11" fill="none" stroke="#fff" stroke-width="2"/><path d="M13 8v10M8 13h10" stroke="#fff" stroke-width="2.2"/></svg>
    New Request
  </a>

  <h2 class="section-title" style="left:406px;top:442px">Recent Completed Requests</h2>
  <div class="box navy" style="left:405px;top:477px;width:387px">
    <table>
      <colgroup><col style="width:186px"><col></colgroup>
      <thead><tr><th>Request No.</th><th>Complete Date</th></tr></thead>
      <tbody>
        <tr><td>56-0001</td><td>20/4/2013</td></tr>
      </tbody>
    </table>
    <div class="pager"><span><svg viewBox="0 0 8 8"><path d="M5 1 2 4l3 3" fill="none" stroke="#a0a5ab"/></svg></span><span class="on">1</span><span>2</span><span>3</span><span>5</span><span>10</span><span>...</span><span class="next"><svg viewBox="0 0 8 8"><path d="M3 1l3 3-3 3" fill="none" stroke="#fff" stroke-width="1.3"/></svg></span></div>
  </div>
</main>

<footer>
  <div class="footer-brand"><span class="brand-dot"></span>VELMORA<br>PETROCHEMICAL</div>
  <p class="copyright">Copyright © 2013 Velmora Petrochemical. All rights reserved.</p>
  <div class="social"><span></span><span></span><span></span><span></span></div>
</footer>
</body>
</html>
```